FItness Bootcamp Flyer

We need an A4 flyer to distribute on an advertising board, and also distribute in the mail.

It should contain a photo(s) of females exercising and having fun outdoors.

It should contain the following text and if you think it could be worded better please change as I'm just looking at getting people to come along:

- TrimPeak Motion Outdoor Bootcamp
Get moving, get fit and feel great

Commencing 19th May

Get results before the winter season
6 Week Bootcamp for $49. Limited numbers!
Or casual visit $10 per session

Now is the time to:
- Lose Weight and Tone-up
- Build Strength and Endurance
- Increase Cardio Fitness
- Improve Your Energy and Vitality
- Fun Varied and Exciting Training Programs
- ALL Fitness Levels

LADIES ONLY BOOTCAMP SUBIACO
Monday 6:30-7:15am, 8:30-9:15am
Wednesday 6:30-7:!5am, 8:30-9:15am
Friday 8:30-9:15am,

Register you place now on 0452 870 214 or email: trimpeakmotion@mailvora.com

facebook.com/TrimPeak Motion

Target Market(s)

Females 20-60yrs

Industry/Entity Type

Advertising

Requirements
Nice to have
• - We like the words and style of the Harbour Ridge Active Training flyer attached
- Also the Velta Group brochure
- I like the colour Blue, Green, Pink. They don't all have to be used but at least one would be nice thank you

```html
<!DOCTYPE html>
<html lang="en">
<head>
<meta charset="utf-8">
<title>TrimPeak Motion Outdoor Bootcamp Flyer</title>
<link href="https://fonts.googleapis.com/css2?family=Source+Sans+3:wght@400;600;700&display=swap" rel="stylesheet">
<style>
  :root {
    --pink: #d5789d;
    --pink-deep: #cf6f95;
    --blue: #5fa9d9;
    --blue-text: #5aa6dc;
    --ink: #1a1a1a;
    --white: #ffffff;
    --paper: #f2f2f2;
    --backdrop: #1e1e1e;
  }
  * { margin: 0; padding: 0; box-sizing: border-box; }
  html, body { width: 1200px; height: 900px; overflow: hidden; background: var(--backdrop); }
  body { font-family: "Source Sans 3", "Segoe UI", sans-serif; position: relative; }

  .flyer {
    position: absolute; left: 350px; top: 103px;
    width: 500px; height: 682px;
    background: var(--paper); overflow: hidden;
  }
  .hero-photo {
    position: absolute; left: 0; top: 0; width: 500px; height: 290px;
    background: linear-gradient(120deg, #cfdde9 0%, #8fb6d8 40%, #e7a9c2 65%, #a9c9e6 100%);
  }
  .side-photo {
    position: absolute; left: 220px; top: 288px; width: 280px; height: 360px;
    background: linear-gradient(180deg, #f4f4f4 0%, #eef1f5 45%, #dfe8f0 100%);
  }
  .shapes { position: absolute; left: 0; top: 0; }

  .brand-title {
    position: absolute; left: 12px; width: 196px; text-align: center;
    font-weight: 600; line-height: 1;
  }
  .brand-name { top: 44px; font-size: 20px; color: var(--blue-text); }
  .brand-sub { top: 67px; font-size: 21px; color: var(--white); }

  .offer {
    position: absolute; left: 25px; top: 283px; width: 195px;
    color: var(--white); font-weight: 600; font-size: 18.5px; line-height: 24.5px;
  }
  .offer .price { color: var(--ink); }

  .start {
    position: absolute; left: 17px; top: 474px; width: 195px; text-align: center;
    color: var(--white); font-weight: 600; font-size: 28px; line-height: 29px;
  }
  .start .day { color: var(--ink); }

  .info { position: absolute; left: 226px; top: 0; width: 274px; }
  .info-head {
    position: absolute; left: 0; color: var(--blue-text);
    font-weight: 600; font-size: 21px; line-height: 1; white-space: nowrap;
  }
  .lead { top: 298px; }
  .class-head { top: 482px; font-size: 19px; }
  .register { top: 581px; }

  .benefits { position: absolute; left: 0; top: 330px; list-style: none; }
  .benefits li {
    position: relative; padding-left: 22px; height: 24.5px;
    font-size: 13px; color: var(--ink); white-space: nowrap; letter-spacing: -0.2px;
  }
  .benefits svg { position: absolute; left: 0; top: 2px; }

  .schedule, .contact {
    position: absolute; left: 21px; font-size: 12.5px; color: var(--ink);
    font-weight: 600; line-height: 24.5px; white-space: nowrap;
  }
  .schedule { top: 503px; }
  .contact { top: 605px; line-height: 22px; font-weight: 400; }

  .tagline {
    position: absolute; left: 0; top: 647px; width: 500px; height: 35px;
    background: var(--pink); color: var(--white); text-align: center;
    font-weight: 600; font-size: 20px; line-height: 35px; letter-spacing: 0.6px;
  }
</style>
</head>
<body>
  <main class="flyer">
    <div class="hero-photo" role="img" aria-label="Photo of women stretching together in a group fitness class"></div>
    <div class="side-photo" role="img" aria-label="Faded photo of a woman lifting light dumbbells"></div>

    <svg class="shapes" width="500" height="682" viewBox="0 0 500 682" aria-hidden="true">
      <polygon points="12,0 207,0 207,100 110,172 12,100" fill="var(--blue)"/>
      <polygon points="12,0 207,0 207,94 110,165 12,94" fill="var(--pink)"/>
      <polygon points="18,287 110,198 215,287 215,437 18,437" fill="var(--pink)"/>
      <polygon points="17,447 212,447 212,549 250,552 128,622 5,549 17,549" fill="var(--blue)"/>
    </svg>

    <div class="brand-title brand-name">TrimPeak Motion</div>
    <div class="brand-title brand-sub">Outdoor Bootcamp</div>

    <p class="offer">Get results before the winter season 6 Week Bootcamp for <span class="price">$49</span>. Limited numbers! Or casual visit <span class="price">$10</span> per session</p>

    <p class="start">Commencing<br><span class="day">19th</span> May</p>

    <section class="info">
      <h2 class="info-head lead">Now is the time to</h2>
      <ul class="benefits">
        <li><svg width="15" height="13" viewBox="0 0 15 13"><path d="M1 7 L5.5 11 L14 1.5" fill="none" stroke="var(--blue)" stroke-width="2.6"/></svg>Lose Weight and Tone-up</li>
        <li><svg width="15" height="13" viewBox="0 0 15 13"><path d="M1 7 L5.5 11 L14 1.5" fill="none" stroke="var(--blue)" stroke-width="2.6"/></svg>Build Strength and Endurance</li>
        <li><svg width="15" height="13" viewBox="0 0 15 13"><path d="M1 7 L5.5 11 L14 1.5" fill="none" stroke="var(--blue)" stroke-width="2.6"/></svg>Increase Cardio Fitness</li>
        <li><svg width="15" height="13" viewBox="0 0 15 13"><path d="M1 7 L5.5 11 L14 1.5" fill="none" stroke="var(--blue)" stroke-width="2.6"/></svg>Improve Your Energy and Vitality</li>
        <li><svg width="15" height="13" viewBox="0 0 15 13"><path d="M1 7 L5.5 11 L14 1.5" fill="none" stroke="var(--blue)" stroke-width="2.6"/></svg>Fun Varied and Exciting Training Programs</li>
        <li><svg width="15" height="13" viewBox="0 0 15 13"><path d="M1 7 L5.5 11 L14 1.5" fill="none" stroke="var(--blue)" stroke-width="2.6"/></svg>ALL Fitness Levels</li>
      </ul>

      <h2 class="info-head class-head">Ladies only bootcamp subiaco</h2>
      <p class="schedule">Monday 6:30-7:15am, 8:30-9:15am<br>Wednesday 6:30-7:!5am, 8:30-9:15am<br>Friday 8:30-9:15am</p>

      <h2 class="info-head register">Register you place now on</h2>
      <p class="contact">0452 870 214 or<br>trimpeakmotion@mailvora.com</p>
    </section>

    <footer class="tagline">Get moving, get fit and feel great</footer>
  </main>
</body>
</html>
```